I'm looking for strong image and design for the first book in a series titled "Bernard Whitcombe On A Voyage Through Our Convictions" subtitle "Finding a Footing in Living"; although it's about beliefs, I'm not look for an ethereal feel as the first book is about how our beliefs impact our actions and expectations. I'm a published philosopher and keen on branding my name for professional purposes hence the use of my name :) The book will initially be an e-book but I will follow up with a paperback soon afterwards. My website http://bernardwhitcombe-example.com/ may provide some help on me and my projects. Thanks, Bern

Target Market(s)

Graduates and corporate folk who tend to lose their way in the systems.

Logo Text

Bernard Whitcombe on Convictions

Font styles to use
Sans Serif

Colors

Designer to choose colors to be used in the design.

Requirements
Must have
• Needless to say, but impact.
Nice to have
• Strong colours
Should not have
• Religious imagery; the book is philosophical and leans into living in this world.

```html
<!DOCTYPE html>
<html lang="en">
<head>
<meta charset="UTF-8">
<title>Bernard Whitcombe On A Voyage Through Our Convictions — Cover</title>
<link rel="stylesheet" href="https://fonts.googleapis.com/css2?family=Russo+One&display=swap">
<style>
  :root {
    --cover-black: #1b1b1b;
    --cover-charcoal: #2f2f2f;
    --type-peach: #ebbca3;
    --type-rose: #d99a8a;
    --portrait-skin-light: #f1cdb8;
    --portrait-skin: #e4b49a;
    --portrait-hair: #a06c45;
    --portrait-hair-dark: #7a4e30;
  }
  * { margin: 0; padding: 0; box-sizing: border-box; }
  html, body {
    width: 1083px;
    height: 1200px;
    overflow: hidden;
    background: var(--cover-black);
  }
  .book-cover {
    position: relative;
    width: 1083px;
    height: 1200px;
    background: linear-gradient(180deg, var(--cover-black) 0%, var(--cover-charcoal) 100%);
    font-family: "Russo One", "Arial Black", sans-serif;
    text-transform: uppercase;
  }
  .portrait-area {
    position: absolute;
    top: 0;
    left: 530px;
    width: 553px;
    height: 1200px;
    background:
      linear-gradient(90deg, transparent 62%, var(--portrait-hair) 82%, var(--portrait-hair-dark) 100%),
      linear-gradient(180deg, var(--portrait-hair) 0%, var(--portrait-skin-light) 22%, var(--portrait-skin) 70%, var(--portrait-skin-light) 100%);
  }
  .title-block {
    position: absolute;
    top: 70px;
    right: 553px;
    text-align: right;
    color: var(--type-peach);
    font-size: 74px;
    line-height: 0.96;
    letter-spacing: 1px;
  }
  .subtitle-block {
    position: absolute;
    top: 790px;
    right: 553px;
    text-align: right;
    color: var(--type-peach);
    font-size: 52px;
    line-height: 1;
    letter-spacing: 1px;
  }
  .subtitle-block .accent { color: var(--type-rose); }
</style>
</head>
<body>
  <main class="book-cover">
    <h1 class="title-block">
      Bern-<br>ard<br>Whit-<br>combe<br>On A<br>Voyage<br>Through<br>Our<br>Convic-<br>tions
    </h1>
    <p class="subtitle-block">
      Finding<br>A Footing<br><span class="accent">In</span><br><span class="accent">Living</span>
    </p>
    <div class="portrait-area" role="img" aria-label="Close-up portrait photograph of a young woman with long auburn hair, half of her face shown"></div>
  </main>
</body>
</html>
```